Landing page для Детский клуб "Тиливки"
Название сайта (домена, или проекта)
Детский клуб "Тиливки"
Цель: Создать современный одностраничный сайт (лендинг) с возможностью в будущем добавлять внутренние страницы. Основная задача — презентовать клуб, его методику и преподавателей, сформировать образ надежного и профессионального детского центра. Итоговая цель — убедить родителей детей 1-7 лет записать ребенка на пробное занятие.
Целевая аудитория: Родители (преимущественно мамы) детей 1-7 лет в Ижевске, для которых важны качество, безопасность, индивидуальный подход, санитарная обработка материалов и профессионализм педагогов.
Детальное ТЗ, логотип, фотографии (для использования на лэндинге) можно найти по ссылке – https://files.nebolka-cloud.ru/d/kqmrtZa-WPn4LH
Адаптивность сайта
Десктопная версия, Версия для планшетов, Версия для телефонов

```html
<!DOCTYPE html>
<html lang="ru">
<head>
<meta charset="utf-8">
<title>Детский клуб "Тиливки"</title>
<link href="https://fonts.googleapis.com/css2?family=Oswald:wght@500;700&family=Montserrat:wght@400;500;600;700&display=swap" rel="stylesheet">
<style>
  :root{
    --cream:#fbf0cc;
    --cream-deep:#f6e3a8;
    --orange:#ff7a4d;
    --orange-dark:#f0602f;
    --pink:#e2418d;
    --pink-soft:#fde3ee;
    --yellow:#f7c23b;
    --ink:#2b2320;
    --muted:#6f6560;
    --white:#ffffff;
    --page:#f4f1ec;
  }
  *{box-sizing:border-box;margin:0;padding:0}
  html,body{width:1200px;height:915px;overflow:hidden}
  body{background:var(--page);font-family:"Montserrat",sans-serif;color:var(--ink)}
  .page{position:relative;width:1200px;height:915px;background:var(--white);overflow:hidden}

  .site-header{position:relative;height:78px;background:var(--white);display:flex;align-items:center;padding:0 60px;gap:34px;z-index:2}
  .brand{display:flex;align-items:center;gap:10px;font-family:"Oswald",sans-serif;font-weight:700;font-size:28px;color:var(--orange);letter-spacing:.5px}
  .brand-dot{width:14px;height:14px;border-radius:50%;background:var(--yellow)}
  .main-nav{display:flex;gap:26px;font-size:13px;font-weight:500}
  .header-contacts{margin-left:auto;display:flex;align-items:center;gap:16px;font-size:13px}
  .address{display:flex;align-items:center;gap:6px;color:var(--muted)}
  .messengers{display:flex;gap:6px}
  .messengers span{width:26px;height:26px;border-radius:50%}
  .m-1{background:#3ea7e0}.m-2{background:#3cc15c}.m-3{background:#3d78d8}
  .phone{font-weight:700}
  .btn{display:inline-block;background:var(--orange);color:var(--white);font-weight:600;border-radius:10px;font-size:13px;padding:12px 20px}

  .hero{position:absolute;left:0;top:78px;width:1200px;height:500px;background:var(--cream)}
  .hero-text{position:absolute;left:60px;top:70px;width:520px}
  .hero-title{font-family:"Oswald",sans-serif;font-weight:700;font-size:56px;line-height:1.02;text-transform:uppercase}
  .hero-title .accent{color:var(--orange)}
  .hero-lead{margin-top:22px;font-size:16px;line-height:1.45;width:400px}
  .hero-cta{margin-top:30px;display:flex;align-items:center;gap:22px}
  .hero-cta .btn{padding:18px 28px;font-size:14px}
  .hero-note{font-size:13px;line-height:1.4;color:var(--muted);width:170px}
  .hero-note b{color:var(--orange);font-weight:600}

  .photo{position:absolute;border:6px solid var(--white);border-radius:26px;box-shadow:0 10px 30px rgba(120,90,30,.15)}
  .photo-1{left:640px;top:90px;width:170px;height:230px;transform:rotate(-7deg);background:linear-gradient(150deg,#f2d9c8,#c9a78f)}
  .photo-2{left:770px;top:60px;width:220px;height:270px;z-index:1;background:linear-gradient(150deg,#d7e7ee,#9fb9c6)}
  .photo-3{left:950px;top:80px;width:180px;height:230px;transform:rotate(7deg);background:linear-gradient(150deg,#efe3cc,#c7a57b)}
  .tagline{position:absolute;left:700px;top:355px;z-index:2;background:var(--white);border-radius:20px;padding:9px 16px;font-size:12px;color:var(--pink);display:flex;align-items:center;gap:8px;box-shadow:0 6px 16px rgba(0,0,0,.06)}

  .clouds{position:absolute;left:0;bottom:-2px;width:1200px;height:90px}

  .why{position:absolute;left:0;top:578px;width:1200px;height:337px;background:var(--white)}
  .why-label{position:absolute;left:60px;top:20px;font-size:12px;color:var(--pink);background:var(--pink-soft);padding:5px 12px;border-radius:14px}
  .why-title{position:absolute;left:60px;top:56px;width:520px;font-family:"Oswald",sans-serif;font-weight:700;font-size:44px;line-height:1.05;text-transform:uppercase}
  .why-title .accent{color:var(--pink)}
  .why-text{position:absolute;left:60px;top:176px;width:430px;font-size:15px;line-height:1.5;color:var(--muted)}

  .card{position:absolute;border-radius:22px}
  .card-photo-kid{left:620px;top:10px;width:260px;height:190px;background:linear-gradient(140deg,#e6f0d8,#a9c98f)}
  .card-feature{background:var(--white);border:1px solid #f0e8e0;box-shadow:0 8px 22px rgba(0,0,0,.05);padding:22px}
  .card-teachers{left:900px;top:10px;width:240px;height:190px}
  .card-method{left:620px;top:218px;width:260px;height:150px}
  .card-shelf{left:900px;top:218px;width:240px;height:150px;background:linear-gradient(150deg,#d9dde6,#8d97a8)}
  .icon-box{width:40px;height:40px;border-radius:10px;display:flex;align-items:center;justify-content:center}
  .icon-pink{background:var(--pink)}
  .icon-yellow{background:var(--yellow)}
  .feature-title{margin-top:14px;font-weight:700;font-size:16px;line-height:1.2}
  .feature-text{margin-top:8px;font-size:12px;line-height:1.4;color:var(--muted)}
</style>
</head>
<body>
<div class="page">

  <header class="site-header">
    <div class="brand"><span class="brand-dot"></span>Тиливки</div>
    <nav class="main-nav">
      <span>Преимущества</span><span>Занятия</span><span>Педагоги</span><span>Отзывы</span><span>Контакты</span>
    </nav>
    <div class="header-contacts">
      <span class="address">
        <svg width="14" height="16" viewBox="0 0 14 16"><path d="M7 1a5 5 0 0 0-5 5c0 4 5 9 5 9s5-5 5-9a5 5 0 0 0-5-5z" fill="none" stroke="#6f6560" stroke-width="1.5"/><circle cx="7" cy="6" r="1.8" fill="#6f6560"/></svg>
        ул. Садовая, 14, Ижевск
      </span>
      <span class="messengers"><span class="m-1"></span><span class="m-2"></span><span class="m-3"></span></span>
      <span class="phone">+7 (900) 555-27-18</span>
      <span class="btn">Позвонить мне</span>
    </div>
  </header>

  <section class="hero">
    <div class="hero-text">
      <h1 class="hero-title">Берём на себя<br><span class="accent">заботу о развитии</span><br>ваших деток</h1>
      <p class="hero-lead">Индивидуальные и групповые развивающие занятия для детей 1-7 лет в Ижевске</p>
      <div class="hero-cta">
        <span class="btn">Записаться на первое занятие</span>
        <p class="hero-note">Записывайтесь на первое занятие <b>со скидкой 20%</b></p>
      </div>
    </div>

    <div class="photo photo-1" role="img" aria-label="Фото: малыш играет с развивающими игрушками"></div>
    <div class="photo photo-2" role="img" aria-label="Фото: педагог занимается с детьми за столом"></div>
    <div class="photo photo-3" role="img" aria-label="Фото: ребёнок собирает деревянный конструктор"></div>
    <div class="tagline">
      <svg width="14" height="12" viewBox="0 0 14 12"><path d="M7 11.5 1.5 6A3.2 3.2 0 0 1 7 2a3.2 3.2 0 0 1 5.5 4z" fill="#e2418d"/></svg>
      С любовью к каждому малышу, с верой в его таланты!
    </div>

    <svg class="clouds" viewBox="0 0 1200 90" preserveAspectRatio="none" aria-hidden="true">
      <path fill="#ffffff" d="M0 60 C40 30 90 30 120 55 C150 20 220 20 250 55 C280 35 330 35 360 60 C400 25 470 25 500 58 C530 38 580 38 610 62 C650 28 720 28 750 58 C780 36 830 36 860 60 C900 26 970 26 1000 57 C1030 36 1080 36 1110 60 C1140 40 1180 40 1200 55 L1200 90 L0 90 Z"/>
    </svg>
  </section>

  <section class="why">
    <span class="why-label">Почему мы</span>
    <h2 class="why-title">Почему родители и дети<br><span class="accent">выбирают именно нас</span></h2>
    <p class="why-text">За 15 лет мы создали атмосферу, в которой дети чувствуют себя любимыми и раскрывают свои таланты.</p>

    <div class="card card-photo-kid" role="img" aria-label="Фото: ребёнок с яркой развивающей игрушкой"></div>
    <div class="card card-feature card-teachers">
      <div class="icon-box icon-pink">
        <svg width="20" height="20" viewBox="0 0 20 20"><circle cx="10" cy="7" r="3.5" fill="#fff"/><path d="M3 17c1-4 4-5.5 7-5.5s6 1.5 7 5.5z" fill="#fff"/></svg>
      </div>
      <p class="feature-title">Педагоги высшего уровня</p>
      <p class="feature-text">Опытные специалисты с профильным образованием и любовью к детям</p>
    </div>
    <div class="card card-feature card-method">
      <div class="icon-box icon-yellow">
        <svg width="20" height="20" viewBox="0 0 20 20"><path d="M3 4h6a2 2 0 0 1 1 1v11a2 2 0 0 0-1-1H3zM17 4h-6a2 2 0 0 0-1 1v11a2 2 0 0 1 1-1h6z" fill="#fff"/></svg>
      </div>
      <p class="feature-title">Авторская методика</p>
      <p class="feature-text">Программа развития, проверенная годами практики</p>
    </div>
    <div class="card card-shelf" role="img" aria-label="Фото: стеллаж с книгами и развивающими пособиями"></div>
  </section>

</div>
</body>
</html>
```